Heron Dusk business card design

I make handmade colourful women's beaded jewellery (necklaces and earnings).
I require a business card to be designed to truly reflect my jewellery, that is, it is different and stands out.
I would like the business card to look creative, arty, gentle and feminine and fit in with the look of my website and logo (already developed).
I would like the business card to have strong use of the water reeds that are flowing in the wind (please see the banner image on my website www.herondusk-example.com and attached files).

Target Market(s)

Women who are fashion conscious, hip and funky. My audience like things that are a little different and stand out in a crowd.These women are aged in their 20's-40's.

Industry/Entity Type

Jewelry

Contact Information for Business Card

Please include the following items:
1) my logo: Heron Dusk
2) my name, address and phone number: Marla Dorsten, Sydney, Australia, 0400 000 000
3) my web details: www.herondusk-example.com, info@herondusk-example.com, www.facebook.com/herondusk

Font styles to use
Other font styles liked:
• Remachine Script

Requirements
Must have
• My business card must have the following:
• 1) my personal details including all my website contacts (see above).
• 2) Heron Dusk logo
• 3) Reeds flowing in the wind (see my banner image on my website www.herondusk-example.com or see attached files).
Nice to have
• A sunrise in the background (rising over water)
• I would prefer that the colour scheme to fit with the Heron Dusk logo, that is the colours of an early morning sunrise i.e yellows, oranges. The use of black and white is fine.
Should not have
• I do not like a commercial manufactured look with hard edges. I would like a look that is soft and reflects an artistic, creative and independent business.

```html
<!DOCTYPE html>
<html lang="en">
<head>
<meta charset="utf-8">
<title>Heron Dusk business card</title>
<link href="https://fonts.googleapis.com/css2?family=Open+Sans:wght@400;600;700&display=swap" rel="stylesheet">
<style>
  :root {
    --stage: #d6d6d4;
    --card-dark: #231f20;
    --card-dark-edge: #3a3536;
    --card-light: #ffffff;
    --accent: #fdc20f;
    --accent-deep: #f0a012;
    --ink: #2a2a2a;
    --ink-soft: #5b5b5b;
    --rule: #4a4a4a;
    --rule-light: #8a8585;
  }
  * { box-sizing: border-box; margin: 0; padding: 0; }
  html, body { width: 1200px; height: 950px; overflow: hidden; }
  body {
    background: var(--stage);
    font-family: "Open Sans", Arial, sans-serif;
    position: relative;
  }
  .card {
    position: absolute;
    left: 220px;
    width: 760px;
    height: 434px;
    border-radius: 4px;
    box-shadow: 0 6px 18px rgba(0,0,0,.18);
    overflow: hidden;
  }
  .card--front {
    top: 28px;
    background: linear-gradient(160deg, var(--card-dark-edge) 0%, var(--card-dark) 55%);
  }
  .card--back {
    top: 488px;
    background: var(--card-light);
  }

  /* brand name as plain text */
  .brand {
    position: absolute;
    font-weight: 600;
    letter-spacing: .5px;
    line-height: 1;
    white-space: nowrap;
  }
  .card--front .brand {
    left: 50%; top: 150px; transform: translateX(-50%);
    font-size: 40px; color: #ffffff;
  }
  .card--back .brand {
    right: 48px; top: 72px;
    font-size: 34px; color: var(--ink);
  }

  /* front social row */
  .social {
    position: absolute;
    left: 0; right: 0; top: 268px;
    height: 40px;
  }
  .social__rule {
    position: absolute; left: 130px; right: 130px; top: 34px; height: 1px;
    background: linear-gradient(90deg, transparent, var(--rule-light) 30%, var(--rule-light) 70%, transparent);
  }
  .social__icons {
    position: absolute; left: 50%; top: 0; transform: translateX(-50%);
    display: flex; gap: 10px;
  }
  .social__icon {
    width: 22px; height: 22px; border-radius: 50%;
    background: var(--accent);
  }

  /* back details */
  .divider {
    position: absolute; left: 190px; right: 48px; top: 212px;
    height: 1.5px; background: var(--rule);
  }
  .person {
    position: absolute; left: 44px; top: 190px;
  }
  .person__name { font-weight: 700; font-size: 24px; color: var(--ink); line-height: 1.1; }
  .person__role { font-size: 18px; color: var(--accent-deep); margin-top: 4px; }
  .address {
    position: absolute; right: 48px; top: 226px;
    text-align: right; font-size: 17px; color: var(--ink-soft); line-height: 1.4;
    font-style: normal;
  }
  .contacts {
    position: absolute; left: 44px; top: 276px;
    list-style: none;
  }
  .contacts li {
    display: flex; align-items: center; gap: 12px;
    font-size: 17px; color: var(--ink-soft); height: 30px;
  }
  .contacts svg { width: 18px; height: 18px; flex: none; }
</style>
</head>
<body>

<section class="card card--front" aria-label="Card front">
  <p class="brand">Heron Dusk</p>
  <div class="social">
    <div class="social__rule"></div>
    <div class="social__icons" aria-label="Social links">
      <span class="social__icon"></span>
      <span class="social__icon"></span>
      <span class="social__icon"></span>
      <span class="social__icon"></span>
    </div>
  </div>
</section>

<section class="card card--back" aria-label="Card back">
  <p class="brand">Heron Dusk</p>

  <div class="divider"></div>

  <div class="person">
    <p class="person__name">Tam Rivers</p>
    <p class="person__role">President</p>
  </div>

  <address class="address">
    Marla Dorsten<br>Sydney, Australia
  </address>

  <ul class="contacts">
    <li>
      <svg viewBox="0 0 18 18" aria-hidden="true"><path fill="#222" d="M4 2h3l1.5 4-2 1.3a9 9 0 0 0 4.2 4.2L12 9.5l4 1.5v3a2 2 0 0 1-2 2A12 12 0 0 1 2 4a2 2 0 0 1 2-2z"/></svg>
      0400 000 000
    </li>
    <li>
      <svg viewBox="0 0 18 18" aria-hidden="true"><rect x="1.5" y="4" width="15" height="10" rx="1" fill="#222"/><path d="M2 5l7 5 7-5" stroke="#fff" stroke-width="1.4" fill="none"/></svg>
      info@herondusk-example.com
    </li>
    <li>
      <svg viewBox="0 0 18 18" aria-hidden="true"><circle cx="9" cy="9" r="7.5" fill="#222"/><ellipse cx="9" cy="9" rx="3" ry="7" stroke="#fff" stroke-width="1.1" fill="none"/><path d="M2 9h14" stroke="#fff" stroke-width="1.1"/></svg>
      www.herondusk-example.com
    </li>
    <li>
      <svg viewBox="0 0 18 18" aria-hidden="true"><rect x="1.5" y="1.5" width="15" height="15" rx="2" fill="#222"/></svg>
      herondusk
    </li>
  </ul>
</section>

</body>
</html>
```